Organic Infographic – "The 4 Dimensions of Transformation"

Overview:
We are a coaching/education brand (Brightmoor Institute) and need a redesigned infographic illustrating our 4-area transformation model. Our current version (attached) uses a rigid, hard-edged triangle/pyramid layout — we want a completely new visual approach that feels organic, soft, and alive, since the topic is human personal development, not a technical process.

Content structure (please keep the wording, redesign the visual form):

4 areas: "Embodiment – The Foundation" and "Focus & Intuition Redefined – The Lens" sit on the same base level. "Heart Centered Living – The Bridge" sits one level above, connecting/enabling the other two. "Becoming Unlimited – The Peak" sits at the top, made possible by Heart Centered Living.
The 4 areas influence and inspire one another — this mutual connection must be visually recognizable (e.g. through overlapping zones, blended color transitions, connecting flowing lines, or similar). Areas may stay visually distinct; the connection between them is what must be shown.
Hierarchy should be expressed mainly through position/arrangement (ascending flow), not through size differences — all 4 areas should carry similar visual weight, since each is equally essential.
A supporting element: "The Brightmoor Methodology" with 3 phases (Phase 1: Awareness & Insight, Phase 2: Integration & Practice, Phase 3: Expansion & Sustainable Growth), each with a short description (text provided below).

Style direction:
Organic, soft, flowing shapes — no sharp angles or rigid geometric triangles. Attached are 3 moodboard references showing the direction we like: overlapping/blended circular shapes, flowing ribbon-style connections, and organic swirl divisions. Please don't copy any of them directly — combine this organic/overlapping visual language with our specific asymmetric hierarchy (2 areas base level + 1 bridge + 1 peak), which none of the references show exactly. This creative translation is the core task.

Icons: Please design one new, unified icon per area (4 total) plus 3 simple icons for the methodology phases — consistent style across all 7, your creative interpretation is welcome.

Typography: Headlines in Arsenal, body text in DM Sans.

Colors: Base palette — Embodiment D09176, Focus & Intuition Redefined B6623E, Heart Centered Living D9866B, Becoming Unlimited 6F7A70, dark text 23211A, light accent EACEC1. Slight adjustments are welcome if they improve visual distinction between areas.

Technical requirements (important):

Final files as vector format (SVG, AI, or EPS), with separated, editable, non-flattened/non-merged layers and paths.
Shapes should consist of simple, closed outline paths — no fine textures, no complex multi-stop gradients, no photorealistic rendering — since the artwork will later be manually redrawn as a whiteboard-animation video.
Primary format: 16:9 landscape. A secondary vertical/mobile version (3 outer areas stacked below the top area) is welcome but optional.

Usage rights: Full commercial usage across website, video, and social media required.

Attachments to include: current draft PDF (for text content and logo reference only — not for layout), our logo file, and the 3 moodboard reference images.

Budget: $100–150 — please let us know if this realistically allows for more designer participation, or advise on adjusting scope/budget

Methodology phase texts (for the 3 supporting icons):

Phase 1: Awareness & Insight
Cultivating self-reflection, identifying patterns, and gaining clarity on personal drivers through introspective practices and data-informed assessment.

Phase 2: Integration & Practice
Applying tools and frameworks, developing new habits, and aligning actions with core values through consistent application and feedback loops.

Phase 3: Expansion & Sustainable Growth
Achieving long-term transformation, exceeding limitations, and fostering resilience through continuous evolution and a purpose-driven approach.

```html
<!DOCTYPE html>
<html lang="en">
<head>
<meta charset="utf-8">
<title>The 4 Dimensions of Transformation – Layout Options</title>
<link rel="stylesheet" href="https://fonts.googleapis.com/css2?family=Arsenal:wght@400;700&family=DM+Sans:wght@300;400;500;600&display=swap">
<style>
  :root{
    --embodiment:#d09176;
    --focus:#b6623e;
    --heart:#d9866b;
    --unlimited:#6f7a70;
    --ink:#23211a;
    --accent:#eacec1;
    --brand:#b9826c;
    --icon-line:#6b6a64;
    --paper:#ffffff;
  }
  html,body{margin:0;padding:0;}
  body{width:1200px;height:1016px;overflow:hidden;background:var(--paper);position:relative;}
  .board{position:absolute;width:560px;height:316px;display:block;}
  .board--a{left:33px;top:26px;}
  .board--b{left:606px;top:26px;}
  .board--c{left:33px;top:350px;}
  .board--d{left:606px;top:350px;}
  .board--e{left:33px;top:676px;}
  .board--f{left:606px;top:676px;}
  .defs-holder{position:absolute;width:0;height:0;overflow:hidden;}

  .title{font-family:"Arsenal",sans-serif;font-weight:700;font-size:36px;fill:var(--ink);}
  .brand{font-family:"DM Sans",sans-serif;font-weight:300;font-size:20px;fill:var(--brand);}
  .brand-dot{fill:var(--brand);}
  .area-name{font-family:"Arsenal",sans-serif;font-weight:700;font-size:20px;fill:#fff;text-anchor:middle;}
  .area-name--sm{font-size:15px;}
  .area-role{font-family:"DM Sans",sans-serif;font-weight:400;font-size:14px;fill:#fff;fill-opacity:.92;text-anchor:middle;}
  .area-role--sm{font-size:12px;}
  .phase-no{font-family:"DM Sans",sans-serif;font-weight:500;font-size:10px;fill:var(--focus);}
  .phase-no--ink{fill:var(--ink);}
  .phase-head{font-family:"Arsenal",sans-serif;font-weight:700;font-size:13.5px;fill:var(--focus);}
  .phase-copy{font-family:"DM Sans",sans-serif;font-weight:400;font-size:8.6px;fill:var(--ink);}
  .center{text-anchor:middle;}
  .rule{stroke:var(--focus);stroke-width:1;fill:none;}
  .divider{stroke:var(--focus);stroke-opacity:.7;stroke-width:1;}
  .glyph{fill:none;stroke:#fff;stroke-width:2.4;stroke-linecap:round;stroke-linejoin:round;}
  .phase-glyph{fill:none;stroke:var(--icon-line);stroke-width:1.5;stroke-linecap:round;stroke-linejoin:round;}
  .badge-ring{stroke:#fff;stroke-width:3;}
  .bar{fill:var(--focus);}
</style>
</head>
<body>

<svg class="defs-holder" aria-hidden="true">
  <defs>
    <radialGradient id="paper-glow" cx="0.5" cy="0.25" r="0.9">
      <stop offset="0" stop-color="#fbf5f2"/>
      <stop offset="1" stop-color="#f5e6df"/>
    </radialGradient>
    <radialGradient id="figure-tone" cx="0.5" cy="0.4" r="0.6">
      <stop offset="0" stop-color="#e2a88f"/>
      <stop offset="1" stop-color="#c97f62"/>
    </radialGradient>

    <!-- area icons -->
    <g id="glyph-target" class="glyph">
      <circle r="12"/><circle r="6"/><circle r="1.6" fill="#fff"/>
      <path d="M0 -17V-12M0 12V17M-17 0H-12M12 0H17"/>
    </g>
    <g id="glyph-heart" class="glyph">
      <path d="M0 11C-14 2-15-8-8-11C-4-13-1-10 0-7C1-10 4-13 8-11C15-8 14 2 0 11Z"/>
    </g>
    <g id="glyph-infinity" class="glyph">
      <path d="M0 0C-4-6-15-8-15 0C-15 8-4 6 0 0C4-6 15-8 15 0C15 8 4 6 0 0Z"/>
    </g>
    <g id="glyph-ground" class="glyph">
      <circle cy="-7" r="4"/>
      <path d="M-9 6C-5 0 5 0 9 6M-13 10C-6 6 6 6 13 10"/>
    </g>

    <!-- phase icons -->
    <g id="phase-bulb" class="phase-glyph">
      <path d="M-6 4C-11-1-10-11 0-11C10-11 11-1 6 4L5 8H-5Z"/>
      <path d="M-4 11.5H4M-2.5 14.5H2.5"/>
      <path d="M-15-3H-12M12-3H15M-11-13L-9-11M11-13L9-11M0-17V-14.5"/>
    </g>
    <g id="phase-gear" class="phase-glyph">
      <circle r="8"/>
      <circle r="3.5"/>
      <path d="M0-12V-8M0 8V12M-12 0H-8M8 0H12M-8.5-8.5L-5.7-5.7M8.5 8.5L5.7 5.7M8.5-8.5L5.7-5.7M-8.5 8.5L-5.7 5.7"/>
    </g>
    <g id="phase-move" class="phase-glyph">
      <path d="M-14 0H-5M5 0H14M0-14V-5M0 5V14"/>
      <path d="M-10-4L-14 0L-10 4M10-4L14 0L10 4M-4-10L0-14L4-10M-4 10L0 14L4 10"/>
    </g>

    <!-- badges -->
    <g id="figure-badge" role="img" aria-label="Human figure with open arms">
      <circle r="36" fill="url(#figure-tone)" class="badge-ring"/>
      <circle r="30" fill="none" stroke="#fff" stroke-opacity=".35" stroke-width="1"/>
    </g>
    <g id="figure-badge-sm" role="img" aria-label="Human figure with open arms">
      <circle r="27" fill="url(#figure-tone)" class="badge-ring"/>
      <circle r="22" fill="none" stroke="#fff" stroke-opacity=".35" stroke-width="1"/>
    </g>

    <!-- fan layout: four soft petals side by side -->
    <g id="fan-diagram">
      <path fill="var(--embodiment)" d="M76 114C92 86 112 90 128 106C152 130 180 156 200 180C216 198 214 214 204 232C196 246 188 262 164 262C124 264 84 264 48 262C26 261 24 246 26 228C28 206 36 186 50 162C58 146 66 130 76 114Z"/>
      <path fill="var(--focus)" d="M118 62C136 38 166 28 196 20C220 14 244 10 258 10C272 10 276 20 276 36C276 76 278 116 276 150C274 176 260 188 240 190C226 192 216 184 204 172C176 146 146 122 118 96C104 84 106 74 118 62Z"/>
      <path fill="var(--heart)" d="M435 62C417 38 387 28 357 20C333 14 309 10 295 10C281 10 277 20 277 36C277 76 275 116 277 150C279 176 293 188 313 190C327 192 337 184 349 172C377 146 407 122 435 96C449 84 447 74 435 62Z"/>
      <path fill="var(--unlimited)" d="M477 114C461 86 441 90 425 106C401 130 373 156 353 180C337 198 339 214 349 232C357 246 365 262 389 262C429 264 469 264 505 262C527 261 529 246 527 228C525 206 517 186 503 162C495 146 487 130 477 114Z"/>

      <g transform="translate(173 35)"><circle r="27" fill="var(--focus)" class="badge-ring"/><use href="#glyph-target"/></g>
      <g transform="translate(373 32)"><circle r="27" fill="var(--heart)" class="badge-ring"/><use href="#glyph-heart"/></g>
      <g transform="translate(510 177)"><circle r="27" fill="var(--unlimited)" class="badge-ring"/><use href="#glyph-infinity"/></g>
      <g transform="translate(43 168)"><circle r="27" fill="var(--embodiment)" class="badge-ring"/><use href="#glyph-ground"/></g>
      <use href="#figure-badge" transform="translate(276 230)"/>

      <text class="area-name" x="209" y="85">Focus &amp;</text>
      <text class="area-name" x="209" y="109">Intuition</text>
      <text class="area-role" x="208" y="137">The Lens</text>
      <text class="area-name" x="356" y="84">Heart Centered</text>
      <text class="area-name" x="356" y="108">Living</text>
      <text class="area-role" x="347" y="138">The Bridge</text>
      <text class="area-name" x="433" y="189">Becoming</text>
      <text class="area-name" x="433" y="213">Unlimited</text>
      <text class="area-role" x="431" y="234">The Peak</text>
      <text class="area-name" x="118" y="208">Embodiment</text>
      <text class="area-role" x="116" y="231">The Foundation</text>
    </g>

    <!-- ascending layout: peak over bridge over two base areas, all soft-edged -->
    <g id="rise-diagram">
      <path fill="var(--accent)" d="M34 292C16 292 12 282 14 266C30 158 120 72 227 72C334 72 424 158 440 266C442 282 438 292 420 292Z"/>
      <path fill="var(--embodiment)" d="M60 292C44 292 38 280 44 262C60 214 82 168 104 156C118 150 130 158 146 180C170 214 196 250 206 270C212 284 204 292 190 292Z"/>
      <path fill="var(--heart)" d="M394 292C410 292 416 280 410 262C394 214 372 168 350 156C336 150 324 158 308 180C284 214 258 250 248 270C242 284 250 292 264 292Z"/>
      <path fill="var(--focus)" d="M150 42C200 30 254 30 304 42C330 48 332 66 316 84C292 110 262 130 227 132C192 130 162 110 138 84C122 66 124 48 150 42Z"/>
      <path fill="var(--unlimited)" d="M170 116C205 104 249 104 284 116C306 124 304 146 292 168C274 204 252 244 236 262C231 268 223 268 218 262C202 244 180 204 162 168C150 146 148 124 170 116Z"/>

      <g transform="translate(227 32)"><circle r="27" fill="var(--focus)" class="badge-ring"/><use href="#glyph-infinity"/></g>
      <g transform="translate(227 130)"><circle r="27" fill="var(--unlimited)" class="badge-ring"/><use href="#glyph-heart"/></g>
      <g transform="translate(380 220)"><circle r="27" fill="var(--heart)" class="badge-ring"/><use href="#glyph-target"/></g>
      <g transform="translate(70 222)"><circle r="27" fill="var(--embodiment)" class="badge-ring"/><use href="#glyph-ground"/></g>
      <use href="#figure-badge-sm" transform="translate(227 288)"/>

      <text class="area-name area-name--sm" x="228" y="78">Becoming Unlimited</text>
      <text class="area-role area-role--sm" x="228" y="95">The Peak</text>
      <text class="area-name area-name--sm" x="228" y="186">Heart Centered</text>
      <text class="area-name area-name--sm" x="228" y="201">Living</text>
      <text class="area-role area-role--sm" x="229" y="221">The</text>
      <text class="area-role area-role--sm" x="229" y="236">Bridge</text>
      <text class="area-name area-name--sm" x="129" y="256">Embodiment</text>
      <text class="area-role area-role--sm" x="127" y="276">The Foundation</text>
      <text class="area-name area-name--sm" x="318" y="234">Focus &amp;</text>
      <text class="area-name area-name--sm" x="318" y="255">Intuition</text>
      <text class="area-role area-role--sm" x="317" y="281">The Lens</text>
    </g>

    <!-- shared pieces -->
    <g id="panel-base">
      <rect width="973" height="548" fill="url(#paper-glow)"/>
      <rect class="bar" y="533" width="973" height="15"/>
    </g>
    <g id="heading-block">
      <text class="title" x="0" y="0">The 4 Dimensions of</text>
      <text class="title" x="0" y="35">Transformation</text>
    </g>
    <g id="brand-mark">
      <circle class="brand-dot" cx="0" cy="0" r="17"/>
      <text class="brand" x="25" y="7">Brightmoor Institute</text>
    </g>

    <!-- methodology strip: arrows from a shared rule -->
    <g id="method-arrows">
      <path class="rule" d="M66 367H908"/>
      <path class="rule" d="M183 367V384M179 379L183 384L187 379M476 367V384M472 379L476 384L480 379M770 367V384M766 379L770 384L774 379"/>
      <line class="divider" x1="330" y1="385" x2="330" y2="515"/>
      <line class="divider" x1="627" y1="385" x2="627" y2="515"/>

      <text class="phase-no center" x="183" y="402">Phase 1</text>
      <use href="#phase-bulb" transform="translate(183 429)"/>
      <text class="phase-head center" x="183" y="464">Awareness &amp; Insight</text>
      <text class="phase-copy center" x="183" y="484">Cultivating self-reflection, identifying patterns and gaining</text>
      <text class="phase-copy center" x="183" y="496">clarity on personal drivers through introspective practices</text>
      <text class="phase-copy center" x="183" y="508">and data-informed assessment.</text>

      <text class="phase-no center" x="476" y="402">Phase 2</text>
      <use href="#phase-gear" transform="translate(476 429)"/>
      <text class="phase-head center" x="476" y="464">Integration &amp; Practice</text>
      <text class="phase-copy center" x="476" y="484">Applying tools and frameworks, developing new habits</text>
      <text class="phase-copy center" x="476" y="496">and aligning actions with core values through consistent</text>
      <text class="phase-copy center" x="476" y="508">application and feedback loops.</text>

      <text class="phase-no center" x="770" y="402">Phase 3</text>
      <use href="#phase-move" transform="translate(770 429)"/>
      <text class="phase-head center" x="770" y="464">Expansion &amp; Sustainable Growth</text>
      <text class="phase-copy center" x="770" y="484">Achieving long-term transformation, exceeding limitations</text>
      <text class="phase-copy center" x="770" y="496">and fostering resilience through continuous evolution and a</text>
      <text class="phase-copy center" x="770" y="508">purpose-driven approach.</text>
    </g>

    <!-- methodology strip: ruled row with icons left -->
    <g id="method-row">
      <path class="rule" d="M0 413H973"/>
      <line class="divider" x1="345" y1="413" x2="345" y2="533"/>
      <line class="divider" x1="650" y1="413" x2="650" y2="533"/>

      <use href="#phase-bulb" transform="translate(66 455)"/>
      <text class="phase-no phase-no--ink" x="96" y="449">Phase 1</text>
      <text class="phase-head" x="96" y="463">Awareness &amp; Insight</text>
      <text class="phase-copy" x="96" y="481">Cultivating self-reflection, identifying patterns and</text>
      <text class="phase-copy" x="96" y="493">gaining clarity on personal drivers through introspective</text>
      <text class="phase-copy" x="96" y="505">practices and data-informed assessment.</text>

      <use href="#phase-gear" transform="translate(388 452)"/>
      <text class="phase-no phase-no--ink" x="419" y="449">Phase 2</text>
      <text class="phase-head" x="419" y="463">Integration &amp; Practice</text>
      <text class="phase-copy" x="419" y="481">Applying tools and frameworks, developing new</text>
      <text class="phase-copy" x="419" y="493">habits and aligning actions with core values through</text>
      <text class="phase-copy" x="419" y="505">consistent application and feedback loops.</text>

      <use href="#phase-move" transform="translate(698 456)"/>
      <text class="phase-no phase-no--ink" x="727" y="449">Phase 3</text>
      <text class="phase-head" x="727" y="463">Expansion &amp; Sustainable Growth</text>
      <text class="phase-copy" x="727" y="481">Achieving long-term transformation, exceeding</text>
      <text class="phase-copy" x="727" y="493">limitations and fostering resilience through continuous</text>
      <text class="phase-copy" x="727" y="505">evolution and a purpose-driven approach.</text>
    </g>
  </defs>
</svg>

<!-- Board A: fan diagram, arrowed methodology -->
<svg class="board board--a" viewBox="0 0 973 548" role="group" aria-label="The 4 Dimensions of Transformation, fan layout">
  <use href="#panel-base"/>
  <use href="#heading-block" transform="translate(52 67)"/>
  <use href="#brand-mark" transform="translate(738 56)"/>
  <use href="#fan-diagram" transform="translate(200 95)"/>
  <use href="#method-arrows"/>
</svg>

<!-- Board B: ascending diagram, arrowed methodology -->
<svg class="board board--b" viewBox="0 0 973 548" role="group" aria-label="The 4 Dimensions of Transformation, ascending layout">
  <use href="#panel-base"/>
  <use href="#heading-block" transform="translate(52 67)"/>
  <use href="#brand-mark" transform="translate(738 56)"/>
  <use href="#rise-diagram" transform="translate(260 50)"/>
  <use href="#method-arrows"/>
</svg>

<!-- Board C: large fan, ruled methodology row -->
<svg class="board board--c" viewBox="0 0 973 548" role="group" aria-label="The 4 Dimensions of Transformation, fan layout with row">
  <use href="#panel-base"/>
  <use href="#heading-block" transform="translate(49 61)"/>
  <use href="#brand-mark" transform="translate(730 50)"/>
  <use href="#fan-diagram" transform="translate(182 109) scale(1.13)"/>
  <use href="#method-row"/>
</svg>

<!-- Board D: large ascending, ruled methodology row -->
<svg class="board board--d" viewBox="0 0 973 548" role="group" aria-label="The 4 Dimensions of Transformation, ascending layout with row">
  <use href="#panel-base"/>
  <use href="#heading-block" transform="translate(49 61)"/>
  <use href="#brand-mark" transform="translate(730 50)"/>
  <use href="#rise-diagram" transform="translate(223 45) scale(1.17)"/>
  <use href="#method-row"/>
</svg>

<!-- Board E: title left, compact fan right -->
<svg class="board board--e" viewBox="0 0 973 548" role="group" aria-label="The 4 Dimensions of Transformation, split fan layout">
  <use href="#panel-base"/>
  <use href="#brand-mark" transform="translate(135 223)"/>
  <text class="title center" x="214" y="292">The 4 Dimensions of</text>
  <text class="title center" x="214" y="327">Transformation</text>
  <use href="#fan-diagram" transform="translate(435 69) scale(0.8)"/>

  <path class="rule" d="M471 292H836"/>
  <path class="rule" d="M471 292V306M467 301L471 306L475 301M654 292V306M650 301L654 306L658 301M836 292V306M832 301L836 306L840 301"/>
  <line class="divider" x1="568" y1="317" x2="568" y2="497"/>
  <line class="divider" x1="751" y1="317" x2="751" y2="497"/>

  <text class="phase-no center" x="471" y="327">Phase 1</text>
  <use href="#phase-bulb" transform="translate(471 367)"/>
  <text class="phase-head center" x="471" y="401">Awareness &amp;</text>
  <text class="phase-head center" x="471" y="418">Insight</text>
  <text class="phase-copy center" x="471" y="438">Cultivating self-reflection,</text>
  <text class="phase-copy center" x="471" y="450">identifying patterns and gaining</text>
  <text class="phase-copy center" x="471" y="462">clarity on personal drivers through</text>
  <text class="phase-copy center" x="471" y="474">introspective practices and</text>
  <text class="phase-copy center" x="471" y="486">data-informed assessment.</text>

  <text class="phase-no center" x="654" y="327">Phase 2</text>
  <use href="#phase-gear" transform="translate(654 367)"/>
  <text class="phase-head center" x="654" y="401">Integration &amp;</text>
  <text class="phase-head center" x="654" y="418">Practice</text>
  <text class="phase-copy center" x="654" y="438">Applying tools and</text>
  <text class="phase-copy center" x="654" y="450">frameworks, developing new habits</text>
  <text class="phase-copy center" x="654" y="462">and aligning actions with core values</text>
  <text class="phase-copy center" x="654" y="474">through consistent application and</text>
  <text class="phase-copy center" x="654" y="486">feedback loops.</text>

  <text class="phase-no center" x="836" y="327">Phase 3</text>
  <use href="#phase-move" transform="translate(836 367)"/>
  <text class="phase-head center" x="836" y="401">Expansion &amp;</text>
  <text class="phase-head center" x="836" y="418">Sustainable Growth</text>
  <text class="phase-copy center" x="836" y="438">Achieving long-term</text>
  <text class="phase-copy center" x="836" y="450">transformation, exceeding limitations</text>
  <text class="phase-copy center" x="836" y="462">and fostering resilience through</text>
  <text class="phase-copy center" x="836" y="474">continuous evolution and a</text>
  <text class="phase-copy center" x="836" y="486">purpose-driven approach.</text>
</svg>

<!-- Board F: title left, compact ascending right -->
<svg class="board board--f" viewBox="0 0 973 548" role="group" aria-label="The 4 Dimensions of Transformation, split ascending layout">
  <use href="#panel-base"/>
  <use href="#brand-mark" transform="translate(135 223)"/>
  <text class="title center" x="214" y="292">The 4 Dimensions of</text>
  <text class="title center" x="214" y="327">Transformation</text>
  <use href="#rise-diagram" transform="translate(439 34) scale(0.935)"/>

  <path class="rule" d="M499 337H809"/>
  <path class="rule" d="M499 337V350M495 345L499 350L503 345M654 324V350M650 345L654 350L658 345M809 337V350M805 345L809 350L813 345"/>
  <line class="divider" x1="581" y1="352" x2="581" y2="507"/>
  <line class="divider" x1="736" y1="352" x2="736" y2="507"/>

  <text class="phase-no center" x="499" y="362">Phase 1</text>
  <use href="#phase-bulb" transform="translate(499 395)"/>
  <text class="phase-head center" x="499" y="426">Awareness &amp;</text>
  <text class="phase-head center" x="499" y="439">Insight</text>
  <text class="phase-copy center" x="499" y="457">Cultivating self-reflection,</text>
  <text class="phase-copy center" x="499" y="467">identifying patterns and gaining</text>
  <text class="phase-copy center" x="499" y="477">clarity on personal drivers through</text>
  <text class="phase-copy center" x="499" y="487">introspective practices and</text>
  <text class="phase-copy center" x="499" y="497">data-informed assessment.</text>

  <text class="phase-no center" x="654" y="362">Phase 2</text>
  <use href="#phase-gear" transform="translate(654 395)"/>
  <text class="phase-head center" x="654" y="426">Integration &amp;</text>
  <text class="phase-head center" x="654" y="439">Practice</text>
  <text class="phase-copy center" x="654" y="457">Applying tools and</text>
  <text class="phase-copy center" x="654" y="467">frameworks, developing new</text>
  <text class="phase-copy center" x="654" y="477">habits and aligning actions with</text>
  <text class="phase-copy center" x="654" y="487">core values through consistent</text>
  <text class="phase-copy center" x="654" y="497">application and feedback loops.</text>

  <text class="phase-no center" x="809" y="362">Phase 3</text>
  <use href="#phase-move" transform="translate(809 395)"/>
  <text class="phase-head center" x="809" y="426">Expansion &amp;</text>
  <text class="phase-head center" x="809" y="439">Sustainable Growth</text>
  <text class="phase-copy center" x="809" y="457">Achieving long-term</text>
  <text class="phase-copy center" x="809" y="467">transformation, exceeding limitations</text>
  <text class="phase-copy center" x="809" y="477">and fostering resilience through</text>
  <text class="phase-copy center" x="809" y="487">continuous evolution and a</text>
  <text class="phase-copy center" x="809" y="497">purpose-driven approach.</text>
</svg>

</body>
</html>
```